Tarwin Project Consulting

I need a logo and business card design for a small business operating in the management consulting and contractor space, predominantly in local and state government. I specialise in project management, financial consulting, people and culture, procurement, ICT transformation and contracting for corporate support areas of organisations.

Industry/Entity Type

Business

```html
<!DOCTYPE html>
<html lang="en">
<head>
<meta charset="utf-8">
<title>Tarwin Project Consulting – Business Card</title>
<link rel="stylesheet" href="https://fonts.googleapis.com/css2?family=Raleway:wght@400;500;700;800&display=swap">
<style>
  :root {
    --canvas: #e6e4e1;
    --card-black: #1f1e1f;
    --brand-red: #ec1c24;
    --brand-grey: #9b9b9c;
    --text-white: #ffffff;
  }
  * { margin: 0; padding: 0; box-sizing: border-box; }
  html, body {
    width: 1200px;
    height: 900px;
    overflow: hidden;
    background: var(--canvas);
    font-family: "Raleway", sans-serif;
  }
  .stage {
    position: relative;
    width: 1200px;
    height: 900px;
  }
  .card {
    position: absolute;
    left: 320px;
    width: 560px;
    height: 320px;
    overflow: hidden;
    background: var(--card-black);
    box-shadow: 0 6px 18px rgba(0,0,0,0.18);
  }
  .card--front { top: 80px; }
  .card--back { top: 500px; }

  .wordmark {
    display: flex;
    align-items: center;
    gap: 12px;
    font-weight: 800;
    color: var(--brand-grey);
    text-transform: uppercase;
    line-height: 1.05;
    white-space: nowrap;
  }
  .wordmark__square {
    flex: none;
    background: var(--brand-red);
  }
  .wordmark__name { display: block; }

  .card--front .wordmark {
    position: absolute;
    left: 50%;
    top: 50%;
    transform: translate(-50%, -50%);
    font-size: 40px;
    letter-spacing: 1px;
    gap: 16px;
  }
  .card--front .wordmark__square { width: 40px; height: 40px; }

  .card__panel {
    position: absolute;
    inset: 0;
    width: 100%;
    height: 100%;
  }
  .card--back .wordmark {
    position: absolute;
    left: 30px;
    top: 138px;
    font-size: 20px;
    letter-spacing: 0.5px;
    gap: 9px;
  }
  .card--back .wordmark__square { width: 20px; height: 20px; }

  .contact-name {
    position: absolute;
    right: 34px;
    top: 24px;
    text-align: right;
    color: var(--text-white);
  }
  .contact-name__person {
    font-weight: 800;
    font-size: 25px;
    letter-spacing: 0.3px;
  }
  .contact-name__role {
    font-weight: 500;
    font-size: 16px;
    margin-top: 2px;
  }
  .contact-address {
    position: absolute;
    right: 34px;
    bottom: 28px;
    text-align: right;
    color: var(--text-white);
    font-weight: 400;
    font-size: 19px;
    line-height: 1.4;
    font-style: normal;
  }
</style>
</head>
<body>
<main class="stage">

  <section class="card card--front" aria-label="Business card front">
    <div class="wordmark">
      <span class="wordmark__square"></span>
      <span class="wordmark__name">Tarwin<br>Project<br>Consulting</span>
    </div>
  </section>

  <section class="card card--back" aria-label="Business card back">
    <svg class="card__panel" viewBox="0 0 560 320" preserveAspectRatio="none" aria-hidden="true">
      <polygon points="262,0 560,0 560,320 236,320" fill="var(--brand-red)"/>
    </svg>

    <div class="wordmark">
      <span class="wordmark__square"></span>
      <span class="wordmark__name">Tarwin Project<br>Consulting</span>
    </div>

    <div class="contact-name">
      <div class="contact-name__person">DANIEL HART</div>
      <div class="contact-name__role">Director</div>
    </div>

    <address class="contact-address">
      22 Marlow Parade<br>
      Castlecrag NSW 2068
    </address>
  </section>

</main>
</body>
</html>
```